Golf Tournament Flyer and Header Needed

Non-profit needs a flyer for their benefit golf tournament - "Wild Socks Charity Golf Classic"

Target Market(s)

Design and Construction industry professionals

Industry/Entity Type

Design and Construction

Colors

Designer to choose colors to be used in the design.

Requirements
Must have
• Date: September 22, 2021, 8:00 AM Shotgun Start, Location: Marrowind Links Club. Q-BevTR Logo
Nice to have
• Would like image of golfers in crazy pants incorporated.

```html
<!DOCTYPE html>
<html lang="en">
<head>
<meta charset="utf-8">
<title>Wild Socks Charity Golf Classic</title>
<link rel="stylesheet" href="https://fonts.googleapis.com/css2?family=Oswald:wght@500;600&family=Open+Sans:wght@400;700;800&display=swap">
<style>
  :root {
    --page: #e4e4e4;
    --blue: #3553a6;
    --blue-deep: #2c4796;
    --navy: #2a3f8f;
    --green: #7ac143;
    --green-light: #a3d13c;
    --white: #ffffff;
    --sky: #8fb5dd;
    --grass: #5f8f3a;
  }
  * { margin: 0; padding: 0; box-sizing: border-box; }
  html, body { width: 951px; height: 1200px; overflow: hidden; background: var(--page); }
  .flyer {
    position: absolute; left: 25px; top: 15px; width: 900px; height: 1170px;
    background: linear-gradient(160deg, var(--blue) 0%, var(--blue-deep) 100%);
    overflow: hidden; font-family: "Open Sans", sans-serif; color: var(--white);
  }
  .shapes { position: absolute; inset: 0; }
  .brand {
    position: absolute; top: 34px; left: 0; width: 100%;
    display: flex; justify-content: center; align-items: center; gap: 16px;
  }
  .brand-dot { width: 62px; height: 62px; border-radius: 50%; background: var(--white); }
  .brand-name { font-family: "Open Sans", sans-serif; font-weight: 700; font-size: 50px; letter-spacing: 0.5px; }
  .title {
    position: absolute; top: 150px; width: 100%; text-align: center;
    font-family: "Oswald", sans-serif; font-weight: 600; font-size: 118px; line-height: 1;
    color: var(--green); letter-spacing: 3px; text-shadow: 0 3px 6px rgba(0,0,0,0.25);
  }
  .subtitle {
    position: absolute; top: 280px; width: 100%; text-align: center;
    font-weight: 800; font-size: 42px; letter-spacing: 0.5px;
  }
  .detail { position: absolute; display: flex; align-items: center; gap: 22px; font-weight: 800; font-size: 29px; }
  .detail-icon {
    width: 64px; height: 64px; border-radius: 50%; background: var(--green);
    display: flex; align-items: center; justify-content: center; flex: none;
  }
  .detail-date { left: 86px; top: 391px; }
  .detail-time { left: 145px; top: 453px; }
  .detail-place { left: 211px; top: 514px; }
  .contact { position: absolute; right: 16px; top: 980px; text-align: right; }
  .contact-call {
    font-family: "Oswald", sans-serif; font-weight: 600; font-size: 24px; line-height: 1.15;
    color: var(--navy); text-transform: uppercase;
  }
  .contact-line { display: flex; justify-content: flex-end; align-items: center; gap: 12px; font-size: 22px; margin-top: 12px; }
</style>
</head>
<body>
<div class="flyer">
  <svg class="shapes" width="900" height="1170" viewBox="0 0 900 1170">
    <defs>
      <linearGradient id="wedge" x1="0" y1="0" x2="1" y2="1">
        <stop offset="0" stop-color="#ffffff" stop-opacity="0.9"/>
        <stop offset="0.6" stop-color="#ffffff" stop-opacity="0.15"/>
        <stop offset="1" stop-color="#ffffff" stop-opacity="0"/>
      </linearGradient>
      <linearGradient id="golfers" x1="0" y1="0" x2="0" y2="1">
        <stop offset="0" stop-color="#3553a6" stop-opacity="0"/>
        <stop offset="0.18" stop-color="#8fb5dd"/>
        <stop offset="0.45" stop-color="#eef0f6"/>
        <stop offset="0.75" stop-color="#7a94c8"/>
        <stop offset="1" stop-color="#5f8f3a"/>
      </linearGradient>
      <linearGradient id="greenband" x1="0" y1="0" x2="1" y2="1">
        <stop offset="0" stop-color="#a3d13c"/>
        <stop offset="1" stop-color="#6dba45"/>
      </linearGradient>
    </defs>
    <polygon points="0,322 420,600 0,600" fill="url(#wedge)"/>
    <rect x="0" y="600" width="900" height="570" fill="url(#golfers)" role="img" aria-label="Photo of four golfers in white shirts and bold blue argyle trousers on a course"/>
    <polygon points="900,560 900,1170 472,1170" fill="url(#greenband)"/>
  </svg>

  <div class="brand"><span class="brand-dot"></span><span class="brand-name">Q-BevTR</span></div>
  <h1 class="title">WILD SOCKS</h1>
  <h2 class="subtitle">CHARITY GOLF CLASSIC</h2>

  <div class="detail detail-date">
    <span class="detail-icon"><svg width="34" height="34" viewBox="0 0 24 24" fill="none" stroke="#fff" stroke-width="2"><rect x="3" y="5" width="18" height="16" rx="1"/><line x1="3" y1="10" x2="21" y2="10"/><line x1="8" y1="3" x2="8" y2="7"/><line x1="16" y1="3" x2="16" y2="7"/></svg></span>
    SEPTEMBER 22, 2021
  </div>
  <div class="detail detail-time">
    <span class="detail-icon"><svg width="36" height="36" viewBox="0 0 24 24" fill="none" stroke="#fff" stroke-width="2"><circle cx="12" cy="12" r="9"/><polyline points="12,7 12,12 15,14"/></svg></span>
    8:00 AM SHOTGUN START
  </div>
  <div class="detail detail-place">
    <span class="detail-icon"><svg width="30" height="30" viewBox="0 0 24 24"><path d="M12 2a7 7 0 0 0-7 7c0 5 7 13 7 13s7-8 7-13a7 7 0 0 0-7-7zm0 9.5a2.5 2.5 0 1 1 0-5 2.5 2.5 0 0 1 0 5z" fill="#fff"/></svg></span>
    LOCATION: MARROWIND LINKS CLUB
  </div>

  <div class="contact">
    <p class="contact-call">For more<br>information<br>please contact us</p>
    <p class="contact-line">555-014-2278 <svg width="20" height="20" viewBox="0 0 24 24"><path d="M6.6 10.8a15 15 0 0 0 6.6 6.6l2.2-2.2a1 1 0 0 1 1-.25 11.4 11.4 0 0 0 3.6.57 1 1 0 0 1 1 1V20a1 1 0 0 1-1 1A17 17 0 0 1 3 4a1 1 0 0 1 1-1h3.5a1 1 0 0 1 1 1c0 1.25.2 2.45.57 3.6a1 1 0 0 1-.25 1z" fill="var(--navy)"/></svg></p>
    <p class="contact-line">www.Q-BevTR.org <svg width="20" height="20" viewBox="0 0 24 24" fill="none" stroke="var(--navy)" stroke-width="2"><circle cx="12" cy="12" r="9"/><line x1="3" y1="12" x2="21" y2="12"/><ellipse cx="12" cy="12" rx="4" ry="9"/></svg></p>
  </div>
</div>
</body>
</html>
```